Restaurant Menu Design - Copper Kettle Noon

We have four items that need to be presented on one page 8 x 11 size with fancy touch. We uploaded 4 photos showing each of the menu items. The photos are intended to be landscape (not portrait) so some of them will need to be turned. The photos may be trimmed if that will aid in the presentation. These are 4 of many items on our menu and these will be featured as "Copper Kettle Noon" (can use the 55 MPH sign or similar concept). The wood grain table background may be changed to a solid color (such as black), so as to sharpen the presentation of the dishes. ALL FOUR PHOTOS MUST BE PRESENTED ON THE DESIGN.

restaurant customer

• Copper Kettle Noon<br/>M-F 11:45 AM to 2:00 PM<br/>$24.99 ea
• wacky, cartoon, silly themes

```html
<!DOCTYPE html>
<html lang="en">
<head>
<meta charset="utf-8">
<title>Copper Kettle Noon – Lunch Deals</title>
<link rel="stylesheet" href="https://fonts.googleapis.com/css2?family=Montserrat:wght@500;700;800;900&display=swap">
<style>
  :root {
    --ink: #111111;
    --board-dark: #1c1c1c;
    --board-mid: #2e2e2e;
    --sun: #fcd116;
    --chili: #a4161a;
    --white: #ffffff;
    --plate: #e9e4da;
    --dish-warm: #b88a5a;
    --dish-cool: #6f86a0;
  }
  * { box-sizing: border-box; margin: 0; padding: 0; }
  html, body { width: 873px; height: 1200px; overflow: hidden; background: var(--ink); }
  .menu {
    position: relative; width: 873px; height: 1200px; overflow: hidden;
    font-family: "Montserrat", Arial, sans-serif;
    background:
      repeating-linear-gradient(90deg, rgba(255,255,255,0.025) 0 2px, transparent 2px 58px),
      linear-gradient(160deg, var(--board-mid), var(--board-dark));
  }

  /* sign */
  .sign {
    position: absolute; left: 82px; top: 79px; width: 358px; height: 354px;
    background: var(--sun); border-radius: 26px; padding: 20px;
  }
  .sign-frame {
    width: 100%; height: 100%;
    border: 9px solid var(--ink); border-radius: 22px;
    display: flex; align-items: center; justify-content: center; text-align: center;
    padding: 20px;
  }
  .sign-name {
    color: var(--ink); font-weight: 800; font-size: 54px; line-height: 1.08;
    text-transform: uppercase; letter-spacing: -1px;
  }

  /* schedule */
  .timing-title {
    position: absolute; left: 45px; top: 545px; width: 430px;
    color: var(--sun); font-weight: 900; font-size: 94px; letter-spacing: 1px;
    line-height: 1; text-align: center;
  }
  .timing-rule {
    position: absolute; left: 45px; top: 644px; width: 425px; height: 5px; background: var(--sun);
  }
  .days {
    position: absolute; left: 41px; top: 696px; width: 441px;
    color: var(--white); font-weight: 500; font-size: 37px; text-align: center; letter-spacing: 0.5px;
  }
  .hours {
    position: absolute; left: 41px; top: 744px; width: 441px; height: 46px;
    background: var(--sun); color: var(--ink);
    font-weight: 800; font-size: 31px; line-height: 46px; text-align: center;
  }

  /* price */
  .price-label {
    position: absolute; left: 106px; top: 841px; width: 329px; height: 86px;
    background: var(--chili); color: var(--white);
    font-weight: 900; font-size: 62px; line-height: 86px; text-align: center;
  }
  .price {
    position: absolute; left: 41px; top: 948px; width: 441px;
    color: var(--white); font-weight: 700; font-size: 86px; text-align: center; letter-spacing: 1px;
  }

  /* deals column */
  .deals { position: absolute; left: 520px; top: 0; width: 353px; height: 1200px; background: var(--sun); }
  .deal-bar {
    position: absolute; left: 0; width: 353px; height: 66px;
    background: var(--ink); color: var(--white);
    font-weight: 800; font-size: 40px; line-height: 66px; text-align: center; letter-spacing: 0.5px;
  }
  .deal-photo {
    position: absolute; left: 55px; width: 243px;
    border-radius: 40px;
    background: radial-gradient(ellipse at 40% 45%, var(--dish-warm), var(--plate) 55%, var(--dish-cool));
  }
</style>
</head>
<body>
<main class="menu">
  <div class="sign"><div class="sign-frame"><span class="sign-name">Copper Kettle Noon</span></div></div>

  <h2 class="timing-title">TIMING</h2>
  <div class="timing-rule"></div>
  <p class="days">MONDAY TO FRIDAY</p>
  <p class="hours">11:45 AM to 2:00 PM</p>

  <div class="price-label">PRICE</div>
  <p class="price">$24.99 ea</p>

  <section class="deals">
    <div class="deal-bar" style="top:0">DEAL ONE</div>
    <div class="deal-photo" style="top:88px;height:214px" role="img" aria-label="Deal one: sashimi plate, hot stone bowl, tempura salad and miso soup"></div>

    <div class="deal-bar" style="top:323px">DEAL TWO</div>
    <div class="deal-photo" style="top:400px;height:215px" role="img" aria-label="Deal two: noodle soup, tempura salad and a long plate of white fish nigiri"></div>

    <div class="deal-bar" style="top:630px">DEAL THREE</div>
    <div class="deal-photo" style="top:708px;height:228px" role="img" aria-label="Deal three: noodle soup, tempura salad and a long plate of assorted nigiri and rolls"></div>

    <div class="deal-bar" style="top:953px">DEAL FOUR</div>
    <div class="deal-photo" style="top:1032px;height:154px" role="img" aria-label="Deal four: noodle soup, steamed rice and a large bowl of poke salad"></div>
  </section>
</main>
</body>
</html>
```